Brand new website for global research and investment startup

We need a simple website, maybe 3 pages: landing page with business description, investment philosophy, team and contact info.
We have a logo already that can be incorporated. Please use the logo only, not the text
We like the color green, something along the lines of #3D6C32 as the main color.
We'd like to design the website with geometric shapes in gradations of the base color. The shapes should suggest "work in progress", "built to last (a long time)", "solidity" and "indestructibility". One idea floating in my head sees smaller features with icosahedron and dodecahedron shapes, and maybe larger structures like crystal lattices; but please feel free to be creative and imagine your own.

```html
<!DOCTYPE html>
<html lang="en">
<head>
<meta charset="utf-8">
<title>Meridian Ridge Capital — Growth That Matters</title>
<link href="https://fonts.googleapis.com/css2?family=Playfair+Display:wght@700;800;900&family=Manrope:wght@400;500;600;700&display=swap" rel="stylesheet">
<style>
:root{
  --stage:#03200e;
  --brand:#3d6c32;
  --brand-mid:#4b9a3c;
  --brand-bright:#58a846;
  --brand-deep:#1f4a1c;
  --ink:#1d3b17;
  --mint:#f3faf0;
  --mint-2:#eef6eb;
  --paper:#ffffff;
  --line:#3d6c32;
  --dark:#062a0f;
  --muted:#3b4a37;
}
*{margin:0;padding:0;box-sizing:border-box}
html,body{width:1200px;height:3064px;overflow:hidden;background:var(--stage)}
body{font-family:"Manrope",Arial,sans-serif;color:var(--ink);position:relative}
.site{position:absolute;left:113px;top:162px;width:974px;height:2866px;background:var(--mint);overflow:hidden}
.abs{position:absolute}
.serif{font-family:"Playfair Display",Georgia,serif;font-weight:900;text-transform:uppercase;letter-spacing:.2px;line-height:1}
.eyebrow{font-size:13px;font-weight:500;color:var(--brand-mid);letter-spacing:.2px;text-transform:uppercase}
.pill{display:inline-flex;align-items:center;gap:4px;border-radius:20px;background:var(--brand-mid);color:#fff;font-size:9.5px;font-weight:600;text-transform:uppercase;justify-content:center;letter-spacing:-.1px}
/* header */
.header{left:0;top:0;width:974px;height:62px;background:#f7f9f6}
.brand{font-family:"Manrope",sans-serif;font-weight:700;font-size:16px;color:var(--brand-deep);display:flex;align-items:center;gap:7px}
.brand i{width:12px;height:12px;background:var(--brand-deep);border-radius:50%;display:block}
.nav{left:318px;top:23px;display:flex;font-size:12.5px;font-weight:500;color:var(--brand-deep)}
.nav span{padding:0 10px;border-left:1.5px solid var(--brand-mid);line-height:17px}
.nav span:first-child{border:none;color:var(--brand-mid)}
.btn-contact{left:762px;top:17px;width:134px;height:30px;background:var(--brand);border-radius:16px;border:2px solid #c9dcc2;color:#fff;font-size:10px;display:flex;align-items:center;justify-content:center}
/* hero */
.hero{left:0;top:62px;width:974px;height:444px;background:#fff}
.hero-art{left:430px;top:66px;width:544px;height:440px;background:radial-gradient(ellipse at 70% 60%,#2f7d2c 0%,#5fae4e 25%,#bfe0b2 50%,rgba(255,255,255,0) 72%)}
.hero-title{left:38px;top:187px;color:var(--brand-deep)}
.hero-title .big{font-size:46px}
.hero-title .mid{font-size:34px;color:var(--brand)}
.hero-title .low{font-size:36px;color:var(--brand-mid);display:block;margin-top:2px}
.hero-rule{left:38px;top:274px;width:114px;height:2px;background:var(--brand-mid)}
.hero-copy{left:38px;top:280px;width:300px;font-size:12.5px;line-height:19px;color:var(--ink)}
.hero-btns{left:38px;top:379px;width:304px;height:38px}
.hero-btns .a{position:absolute;left:0;top:0;width:152px;height:38px;border-radius:20px 0 0 20px;background:var(--brand-mid)}
.hero-btns .b{position:absolute;left:152px;top:0;width:152px;height:38px;border-radius:0 20px 20px 0;background:var(--brand-deep)}
.hero-btns .t{position:absolute;top:13px;color:#fff;font-size:9px;font-weight:600}
.hero-btns .or{position:absolute;left:139px;top:6px;width:26px;height:26px;border-radius:50%;background:#fff;border:2px solid var(--brand-deep);font-size:8px;display:flex;align-items:center;justify-content:center;color:var(--ink)}
/* band */
.band{left:0;top:506px;width:974px;height:62px;background:var(--brand);color:#fff;display:flex;align-items:center}
.band-title{font-family:"Playfair Display",serif;font-weight:700;text-transform:uppercase;font-size:15px;line-height:16px;margin-left:36px;width:232px}
.band-sep{width:1px;height:34px;background:#cfe2c8;margin:0 22px 0 32px}
.band-item{display:flex;align-items:center;gap:8px;font-size:12px;font-weight:600;margin-right:22px}
/* approach */
.approach-eyebrow{left:0;width:974px;top:610px;text-align:center;text-transform:uppercase}
.approach-title{left:0;width:974px;top:640px;text-align:center;font-size:23px;color:var(--brand-deep)}
.card{width:287px;height:143px;border:1.5px solid var(--brand);border-radius:6px;background:var(--mint);text-align:center;padding-top:18px}
.card h3{font-size:14.5px;font-weight:500;color:var(--ink);margin-top:8px}
.card p{font-size:10px;line-height:15px;color:var(--muted);margin:8px auto 0;width:250px}
/* why */
.why{left:0;top:1075px;width:974px;height:309px;background:#f1f6ee}
.why-title{left:42px;top:1155px;font-size:22px;line-height:23px;color:var(--brand-deep)}
.why-list{left:42px;top:1211px;width:437px;height:87px;background:#fff;border-left:1.5px solid var(--brand);border-radius:6px;padding:8px 0 0 20px;font-size:10px;line-height:15px;color:var(--ink)}
.why-list li{margin-left:12px}
.chart-card{left:495px;top:1124px;width:442px;height:215px;background:#fff;border-radius:8px;box-shadow:0 2px 10px rgba(30,70,20,.08)}
/* philosophy */
.philo{left:0;top:1384px;width:974px;height:420px;background:radial-gradient(ellipse at 80% 40%,#11591a 0%,#0a3a12 45%,var(--dark) 100%)}
.philo-art{left:700px;top:1398px;width:190px;height:380px;background:linear-gradient(180deg,rgba(80,255,60,.0) 0%,rgba(70,220,50,.45) 35%,rgba(40,160,30,.35) 70%,rgba(10,60,15,0) 100%);border-radius:40px}
.white{color:#fff}
.pcol{width:200px;text-align:center;color:#fff}
.pcol .ic{width:62px;height:62px;border-radius:50%;background:#2f6a2c;margin:0 auto;display:flex;align-items:center;justify-content:center;border:1px solid #4c8a45}
.pcol h4{font-size:12.5px;font-weight:500;margin-top:13px}
.pcol p{font-size:10px;line-height:15px;margin-top:8px}
.pdiv{width:1px;height:160px;background:#8ca986}
/* insights */
.ins-title{left:75px;top:1878px;font-size:21px;color:var(--brand-deep)}
.icard{width:215px;height:189px;background:var(--brand);border-radius:6px;top:2122px}
.iimg{top:1989px;width:177px;height:177px}
.icard .tag{position:absolute;left:19px;top:59px;height:15px;padding:0 28px;border-radius:8px;background:#8ebf7e;color:#fff;font-size:8.5px;display:flex;align-items:center}
.icard h5{position:absolute;left:19px;top:89px;width:180px;font-family:"Playfair Display",serif;font-weight:700;font-size:11.5px;line-height:12px;color:#fff}
.icard p{position:absolute;left:19px;width:180px;font-size:10px;line-height:15px;color:#fff}
.icard .arr{position:absolute;left:19px;color:#fff;font-size:11px}
/* cta */
.cta{left:0;top:2357px;width:974px;height:246px;background:linear-gradient(90deg,#031f0b 0%,#06280e 45%,#0a3a12 100%)}
.cta-art{left:560px;top:2370px;width:380px;height:225px;background:radial-gradient(ellipse at 70% 55%,rgba(60,230,40,.55) 0%,rgba(30,140,30,.3) 40%,rgba(0,0,0,0) 72%)}
.cta-copy{left:38px;top:2449px;width:420px;border-left:1.5px solid #8ca986;padding-left:8px;font-size:12.5px;line-height:19px;color:#fff}
/* footer */
.foot-desc{left:42px;top:2709px;width:241px;height:81px;background:#fff;border-left:1.5px solid var(--brand);border-radius:6px;padding:7px 8px;font-size:10px;line-height:15px;color:var(--ink)}
.fdiv{width:1px;height:143px;background:var(--brand);top:2648px}
.fhead{font-size:13.5px;font-weight:500;color:var(--brand-mid);top:2649px}
.flist{font-size:10px;line-height:21.5px;color:var(--ink);list-style:none}
.flist li{display:flex;align-items:center;gap:6px}
.dot{width:7px;height:7px;border-radius:50%;border:2px solid var(--brand-deep)}
.social{display:flex;gap:10px;top:2768px;left:691px}
.social i{width:9px;height:9px;background:var(--brand-deep);display:block;border-radius:1px}
.copy{left:0;width:974px;top:2810px;text-align:center;font-size:10px;color:var(--ink)}
</style>
</head>
<body>
<div class="site">

  <!-- header -->
  <div class="abs header"></div>
  <div class="abs brand" style="left:80px;top:21px"><i></i>Meridian Ridge</div>
  <nav class="abs nav"><span>HOME</span><span>PHILOSHOPY</span><span>BLOGS</span><span>TEAM</span><span>CONTACT</span></nav>
  <div class="abs btn-contact">CONTACT US ⊕</div>

  <!-- hero -->
  <div class="abs hero"></div>
  <div class="abs hero-art" role="img" aria-label="Flowing green waves rising into a candlestick chart with an upward arrow"></div>
  <div class="abs eyebrow" style="left:38px;top:158px;font-size:13px">Smart decisions. Stronger futures.</div>
  <div class="abs serif hero-title"><span class="big">Growth</span> <span class="mid">that</span><span class="low">Matters</span></div>
  <div class="abs hero-rule"></div>
  <p class="abs hero-copy">We empower businesses and investors with data-driven insights and innovative strategies to achieve sustainable, long-term growth.</p>
  <div class="abs hero-btns">
    <div class="a"></div><div class="b"></div>
    <span class="t" style="left:30px">OUR PHILOSOPHY →</span>
    <span class="t" style="left:192px">GET STARTED →</span>
    <span class="or">Or</span>
  </div>

  <!-- band -->
  <div class="abs band">
    <div class="band-title">A Disciplined approach to research and investment.</div>
    <div class="band-sep"></div>
    <div class="band-item"><svg width="26" height="26" viewBox="0 0 26 26" fill="none" stroke="#fff" stroke-width="1.4"><circle cx="10" cy="10" r="6"/><path d="M15 15l7 7"/><circle cx="10" cy="10" r="2"/></svg>Research-Driven</div>
    <div class="band-item"><svg width="28" height="28" viewBox="0 0 28 28" fill="none" stroke="#fff" stroke-width="1.4"><circle cx="14" cy="14" r="11"/><circle cx="14" cy="14" r="5"/><path d="M14 0v6M14 22v6M0 14h6M22 14h6"/></svg>Long-Term Focus</div>
    <div class="band-item"><svg width="30" height="28" viewBox="0 0 30 28" fill="none" stroke="#fff" stroke-width="1.4"><rect x="2" y="14" width="6" height="12"/><rect x="11" y="10" width="6" height="16"/><rect x="20" y="6" width="6" height="20"/><path d="M2 10l8-6 6 4 10-7"/></svg>Aligned Interests</div>
    <div class="band-item"><svg width="24" height="28" viewBox="0 0 24 28" fill="none" stroke="#fff" stroke-width="1.4"><path d="M12 2l9 4v8c0 6-4 10-9 12-5-2-9-6-9-12V6z"/><path d="M7 14l4 4 6-7"/></svg>Risk-Aware</div>
  </div>

  <!-- approach -->
  <div class="abs eyebrow approach-eyebrow">Our Approach</div>
  <div class="abs serif approach-title">Principled. Disciplined. Focused.</div>

  <div class="abs card" style="left:39px;top:723px">
    <svg width="32" height="30" viewBox="0 0 32 30" fill="none" stroke="#3d6c32" stroke-width="1.2"><rect x="3" y="16" width="4" height="10"/><rect x="9" y="11" width="4" height="15"/><rect x="15" y="7" width="4" height="19"/><circle cx="24" cy="20" r="6"/><path d="M3 10l7-6 5 3 7-6"/></svg>
    <h3>Invest With Founders</h3><p>We partner with visionary founders and management teams aligned with our long-term mindset.</p></div>
  <div class="abs card" style="left:345px;top:723px">
    <svg width="32" height="30" viewBox="0 0 32 30" fill="none" stroke="#3d6c32" stroke-width="1.2"><path d="M3 14l8-6 6 3 6-3 6 6-10 9-6-5"/><circle cx="16" cy="6" r="4"/></svg>
    <h3>Exceptional Businesses</h3><p>We seek sustainable competitive advantages and strong compounding potential.</p></div>
  <div class="abs card" style="left:650px;top:723px">
    <svg width="32" height="30" viewBox="0 0 32 30" fill="none" stroke="#3d6c32" stroke-width="1.2"><rect x="5" y="4" width="18" height="22" rx="2"/><path d="M9 10h10M9 14h10M9 18h6"/><circle cx="24" cy="21" r="5"/></svg>
    <h3>Long-Term Success</h3><p>We focus on enduring value creation and the ability to thrive across cycles.</p></div>
  <div class="abs card" style="left:39px;top:889px">
    <svg width="32" height="30" viewBox="0 0 32 30" fill="none" stroke="#3d6c32" stroke-width="1.2"><path d="M12 28v-9l-3-4v-4M12 19V8a2 2 0 014 0v9l5 1v10"/><circle cx="25" cy="6" r="4"/></svg>
    <h3>Valuation-Sensitive</h3><p>We invest at prices that provide a margin of safety and attractive return potential.</p></div>
  <div class="abs card" style="left:345px;top:889px">
    <svg width="32" height="30" viewBox="0 0 32 30" fill="none" stroke="#3d6c32" stroke-width="1.2"><circle cx="16" cy="15" r="12"/><circle cx="16" cy="15" r="8"/><path d="M16 10v10M14 12h4M14 18h4"/></svg>
    <h3>Conviction-Sizing</h3><p>We size positions based on our highest convictions and risk-adjusted outlook.</p></div>
  <div class="abs card" style="left:650px;top:889px">
    <svg width="32" height="30" viewBox="0 0 32 30" fill="none" stroke="#3d6c32" stroke-width="1.2"><circle cx="16" cy="10" r="6"/><path d="M4 16l8 10h8l8-10M16 7v6"/></svg>
    <h3>Diversified Excellence</h3><p>We diversify across sectors and value drivers to build resilient, high-quality portfolios.</p></div>

  <!-- why -->
  <div class="abs why"></div>
  <div class="abs eyebrow" style="left:42px;top:1125px">Why partner with us</div>
  <div class="abs serif why-title">A modern approach to global<br>investing.</div>
  <ul class="abs why-list">
    <li>Deep, original research and rigorous analysis</li>
    <li>Disciplined process with a long-term perspective</li>
    <li>Focus on quality, sustainability and governance</li>
    <li>Aligned with local insights and global reach</li>
    <li>UCITS compliant frameworks</li>
  </ul>
  <div class="abs pill" style="left:42px;top:1313px;width:126px;height:24px">Contact with us →</div>

  <div class="abs chart-card">
    <div class="abs serif" style="left:19px;top:20px;font-size:21px;color:var(--brand-deep)">Built for long-term impact</div>
    <p class="abs" style="left:19px;top:51px;width:300px;font-size:10px;line-height:15px;color:var(--muted)">Our goal is simple: to compound value by backing exceptional businesses with durable competitive advantages.</p>
    <div class="abs" style="left:19px;top:107px;font-size:10px;color:var(--muted)"><span style="display:inline-block;width:14px;height:1.5px;background:var(--brand-mid);vertical-align:middle;margin-right:6px"></span>Long-Term Value</div>
    <div class="abs" style="left:19px;top:135px;font-size:10px;color:var(--muted)"><span style="display:inline-block;width:14px;height:1.5px;background:#555;vertical-align:middle;margin-right:6px"></span>Market Average</div>
    <svg class="abs" style="left:0;top:0" width="442" height="215" viewBox="0 0 442 215">
      <defs><linearGradient id="areaFill" x1="0" y1="0" x2="0" y2="1"><stop offset="0" stop-color="#58a846" stop-opacity=".35"/><stop offset="1" stop-color="#58a846" stop-opacity="0"/></linearGradient></defs>
      <path d="M0 212L32 202 100 154 132 148 190 130 238 101 302 94 346 70 380 62 430 16V215H0Z" fill="url(#areaFill)"/>
      <polyline points="0,212 32,202 100,154 132,148 190,130 238,101 302,94 346,70 380,62 430,16" fill="none" stroke="#3d8a32" stroke-width="2"/>
      <g fill="#3d8a32"><circle cx="100" cy="154" r="3"/><circle cx="132" cy="148" r="3"/><circle cx="190" cy="130" r="3"/><circle cx="238" cy="101" r="3"/><circle cx="302" cy="94" r="3"/><circle cx="346" cy="70" r="3"/><circle cx="380" cy="62" r="3"/></g>
      <path d="M422 14l9 1-4 8" fill="none" stroke="#3d8a32" stroke-width="2"/>
      <polyline points="0,198 30,192 105,178 150,182 218,164 260,172 305,152 355,160 385,152 420,166 440,140" fill="none" stroke="#666" stroke-width="1.3"/>
    </svg>
  </div>

  <!-- philosophy -->
  <div class="abs philo"></div>
  <div class="abs philo-art" role="img" aria-label="Glowing green upward arrows over a digital grid"></div>
  <div class="abs white" style="left:38px;top:1427px;font-size:13px;font-weight:500">OUR INVESTMENT PHILOSOPHY</div>
  <div class="abs serif white" style="left:38px;top:1456px;font-size:22px;line-height:23px">We invest with clarity, conviction and<br>discipline.</div>
  <p class="abs white" style="left:38px;top:1516px;font-size:10px">Our approach is grounded in fundamental research, thoughtful risk management, and a commitment to long-term outcomes.</p>
  <div class="abs pcol" style="left:44px;top:1572px"><div class="ic"><svg width="34" height="30" viewBox="0 0 34 30" fill="none" stroke="#fff" stroke-width="1.3"><circle cx="12" cy="14" r="7"/><circle cx="21" cy="17" r="7"/><path d="M26 22l5 5"/></svg></div><h4>Clarity</h4><p>We seek to understand the true drivers of a business.</p></div>
  <div class="abs pdiv" style="left:244px;top:1556px"></div>
  <div class="abs pcol" style="left:256px;top:1572px"><div class="ic"><svg width="32" height="32" viewBox="0 0 32 32" fill="none" stroke="#fff" stroke-width="1.3"><circle cx="16" cy="16" r="12"/><circle cx="16" cy="16" r="7"/><circle cx="16" cy="16" r="2"/><path d="M16 16l11-11"/></svg></div><h4>Conviction</h4><p>We back what we know, and size it accordingly.</p></div>
  <div class="abs pdiv" style="left:455px;top:1556px"></div>
  <div class="abs pcol" style="left:468px;top:1572px"><div class="ic"><svg width="30" height="30" viewBox="0 0 30 30" fill="none" stroke="#fff" stroke-width="1.3"><circle cx="15" cy="15" r="5"/><path d="M15 3v5M15 22v5M3 15h5M22 15h5M7 7l3 3M20 20l3 3M23 7l-3 3M7 23l3-3"/></svg></div><h4>Discipline</h4><p>We manage risk carefully to protect and grow capital.</p></div>
  <div class="abs pill" style="left:38px;top:1737px;width:127px;height:23px">Contact with us →</div>

  <!-- insights -->
  <div class="abs eyebrow" style="left:0;width:974px;top:1844px;text-align:center">Latest Insights</div>
  <div class="abs serif ins-title">Thoughts on markets, business and long-term value.</div>
  <div class="abs pill" style="left:771px;top:1878px;width:127px;height:24px">View all insights →</div>

  <div class="abs icard" style="left:39px"><span class="tag">MARKET</span><h5>The Power Of Compounding</h5><p style="top:117px">Why time, quality and patience are the most powerful allies in investing.</p><span class="arr" style="top:150px">→</span></div>
  <div class="abs iimg" role="img" aria-label="Green bar chart with a rising arrow" style="left:58px;background:linear-gradient(160deg,#0b4a12 0%,#17801d 50%,#36d12a 100%)"></div>
  <div class="abs icard" style="left:267px"><span class="tag">ANALYSIS</span><h5>Quality Businesses, Enduring Advantage</h5><p style="top:129px">What truly sets great companies apart across market cycles.</p><span class="arr" style="top:162px">→</span></div>
  <div class="abs iimg" role="img" aria-label="Golden-green arrows climbing over a glowing chart" style="left:286px;background:radial-gradient(circle at 65% 55%,#b7d93a 0%,#3d8f22 40%,#0a3a12 100%)"></div>
  <div class="abs icard" style="left:495px"><span class="tag">PERSPECTIVES</span><h5>Thinking In Decades, Not Quarters</h5><p style="top:129px">A long-term mindset for navigating uncertainty and opportunity.</p><span class="arr" style="top:162px">→</span></div>
  <div class="abs iimg" role="img" aria-label="Bright green zigzag line rising upward" style="left:514px;background:radial-gradient(circle at 55% 65%,#3cf02a 0%,#137a18 40%,#052a0b 100%)"></div>
  <div class="abs icard" style="left:723px"><span class="tag">INVEST</span><h5>Investing Through Cycles</h5><p style="top:117px">How a disciplined, long-term approach can help investors remain</p><span class="arr" style="top:150px">→</span></div>
  <div class="abs iimg" role="img" aria-label="Green wave curving into an upward arrow" style="left:742px;background:radial-gradient(circle at 50% 60%,#2fc526 0%,#0f6516 45%,#05280b 100%)"></div>

  <!-- cta -->
  <div class="abs cta"></div>
  <div class="abs cta-art" role="img" aria-label="Green arrows rising above a city of digital light"></div>
  <div class="abs serif white" style="left:38px;top:2372px;font-size:28px;line-height:28px">Let’s build long-term<br>value together.</div>
  <div class="abs cta-copy">We welcome conversations with like-minded partners and investors.<br><b style="font-weight:700">Whether you share our long-term perspective, are exploring new investment opportunities, or would like to learn more about our approach, we would be pleased to connect and start a meaningful conversation.</b></div>
  <div class="abs pill" style="left:38px;top:2568px;width:127px;height:24px">Contact with us →</div>

  <!-- footer -->
  <div class="abs brand" style="left:50px;top:2664px"><i></i>Meridian Ridge</div>
  <div class="abs foot-desc">Meridian Ridge Capital is a global research and investment firm focused on identifying exceptional businesses and participating in their long-term success.</div>
  <div class="abs fdiv" style="left:329px"></div>
  <div class="abs fhead" style="left:386px">COMPANY</div>
  <ul class="abs flist" style="left:386px;top:2676px">
    <li><span class="dot"></span>HOME</li><li><span class="dot"></span>PHILOSOPHY</li><li><span class="dot"></span>INSIGHTS</li><li><span class="dot"></span>TEAM</li><li><span class="dot"></span>CONTACT</li>
  </ul>
  <div class="abs fdiv" style="left:634px"></div>
  <div class="abs fhead" style="left:691px">GET IN TOUCH</div>
  <ul class="abs flist" style="left:691px;top:2676px">
    <li><svg width="8" height="10" viewBox="0 0 8 10"><path d="M4 0a4 4 0 014 4c0 3-4 6-4 6S0 7 0 4a4 4 0 014-4z" fill="#1f4a1c"/><circle cx="4" cy="4" r="1.4" fill="#fff"/></svg>Your Adress Will Be Here</li>
    <li><svg width="9" height="7" viewBox="0 0 9 7"><rect width="9" height="7" fill="#1f4a1c"/><path d="M0 0l4.5 4L9 0" stroke="#fff" fill="none"/></svg>info@meridianridge-capital.com</li>
    <li><svg width="8" height="8" viewBox="0 0 8 8"><path d="M1 0l2 2-1 1.5a5 5 0 002.5 2.5L6 5l2 2-1 1C3 8 0 5 0 1z" fill="#1f4a1c"/></svg>+1 555 014 2210</li>
    <li><svg width="8" height="8" viewBox="0 0 8 8"><circle cx="4" cy="4" r="4" fill="#1f4a1c"/></svg>+1 555 014 7788</li>
  </ul>
  <div class="abs social"><i></i><i></i><i></i></div>
  <div class="abs copy">Copyright © 2026 Meridian Ridge Capital | Powered by Meridian Ridge Capital</div>
</div>
</body>
</html>
```